Game, Voice & Dedicated Server Company Needs a Business Card Design

We need a new business card design, centered around our new logo (PSD provided below).

Designs that we do like:
https://pixelmarsh.net/item/corporate-business-card/5382017?s_rank=43 (needs to be made more eye catching)

Our main areas of business are:
- Dedicated Servers
- Game Servers
- Voice Servers
- Mitigation Security Specialists

Industry/Entity Type

Business

Contact Information for Business Card

On the card: (and anything else you would suggest)
- Staff member name
- Staff member position in company
- Staff member phone number
- Staff member email
- Other / Staff member Skype
- Website link

Colors
9bcb3c
abd036

Requirements
Must have
• Design of Card:
• - Green (same green as the logo)
• - Business / Corporate design
• - Something a little different / abstract that shouts premium

```html
<!DOCTYPE html>
<html lang="en">
<head>
<meta charset="utf-8">
<title>Kestrel Hosting – Business Card</title>
<link href="https://fonts.googleapis.com/css2?family=Arimo:wght@400;700&display=swap" rel="stylesheet">
<style>
  :root{
    --bg:#d9d6d0;
    --card-black:#0b0b0b;
    --card-black-2:#1c1c1c;
    --green:#9bcb3c;
    --green-light:#bfe07a;
    --grey-light:#d2d2d2;
    --grey-dark:#8e8e8e;
    --white:#ffffff;
    --muted:#c9c9c9;
  }
  *{margin:0;padding:0;box-sizing:border-box}
  html,body{width:1200px;height:858px;overflow:hidden}
  body{
    background:var(--bg);
    font-family:"Arimo",Arial,sans-serif;
    position:relative;
  }
  .card{
    position:absolute;
    top:274px;
    width:540px;height:310px;
    border-radius:4px;
    overflow:hidden;
    background:linear-gradient(135deg,var(--card-black-2) 0%,var(--card-black) 55%);
    box-shadow:0 10px 28px rgba(0,0,0,.35);
  }
  .card--front{left:40px}
  .card--back{left:620px}

  .card-bands{position:absolute;inset:0;width:100%;height:100%}

  .brand{
    position:absolute;
    display:flex;align-items:center;gap:10px;
    color:var(--green);
    font-weight:700;
    text-transform:uppercase;
    letter-spacing:-0.5px;
  }
  .brand-mark{width:14px;height:14px;background:var(--green)}
  .card--front .brand{left:34px;top:52px;font-size:30px}

  .staff{position:absolute;right:30px;top:36px;text-align:right;color:var(--white)}
  .staff-name{font-size:22px;font-weight:400}
  .staff-role{font-size:12px;color:var(--muted);margin-top:3px}

  .services{
    position:absolute;left:30px;top:192px;
    list-style:none;color:var(--white);font-size:13px;line-height:24px;
  }
  .services li::before{content:"\2605";margin-right:10px;font-size:12px}

  .contacts{
    position:absolute;right:28px;top:170px;
    list-style:none;color:var(--white);font-size:13px;line-height:26px;
  }
  .contacts li{display:flex;align-items:center;gap:10px}
  .contacts svg{width:14px;height:14px;flex:none}

  .card--back .brand{
    left:50%;top:50%;transform:translate(-50%,-50%);
    font-size:40px;
  }
  .card--back .brand-mark{width:18px;height:18px}
</style>
</head>
<body>

<section class="card card--front" aria-label="Business card front">
  <svg class="card-bands" viewBox="0 0 540 310" preserveAspectRatio="none" aria-hidden="true">
    <defs>
      <linearGradient id="greenBand" x1="0" y1="0" x2="1" y2="1">
        <stop offset="0" stop-color="var(--green-light)"/>
        <stop offset="1" stop-color="var(--green)"/>
      </linearGradient>
      <linearGradient id="greyBand" x1="0" y1="0" x2="1" y2="1">
        <stop offset="0" stop-color="var(--grey-dark)"/>
        <stop offset=".5" stop-color="var(--grey-light)"/>
        <stop offset="1" stop-color="var(--grey-dark)"/>
      </linearGradient>
    </defs>
    <polygon class="band-green" points="0,168 312,150 262,310 0,310" fill="url(#greenBand)"/>
    <polygon class="band-grey" points="322,150 540,112 540,310 272,310" fill="url(#greyBand)"/>
  </svg>

  <div class="brand"><span class="brand-mark"></span>Kestrel Hosting</div>

  <div class="staff">
    <p class="staff-name">Marcus Hale</p>
    <p class="staff-role">Managing Director</p>
  </div>

  <ul class="services">
    <li>Dedicated Servers</li>
    <li>Game Servers</li>
    <li>Voice Servers</li>
    <li>Mitigation Security Specialists</li>
  </ul>

  <ul class="contacts">
    <li><svg viewBox="0 0 16 16"><path d="M4 1l3 3-2 2c1 2 3 4 5 5l2-2 3 3-2 3C7 15 1 9 1 3z" fill="#fff"/></svg>000 000 0000</li>
    <li><svg viewBox="0 0 16 16"><rect x="1" y="3" width="14" height="10" fill="none" stroke="#fff" stroke-width="1.5"/><path d="M1 3l7 6 7-6" fill="none" stroke="#fff" stroke-width="1.5"/></svg>hello@kestrelhost.com</li>
    <li><svg viewBox="0 0 16 16"><circle cx="8" cy="8" r="7" fill="#fff"/></svg>kestrelhost</li>
    <li><svg viewBox="0 0 16 16"><circle cx="8" cy="8" r="6.5" fill="none" stroke="#fff" stroke-width="1.3"/><path d="M1.5 8h13M8 1.5c3 3 3 10 0 13M8 1.5c-3 3-3 10 0 13" fill="none" stroke="#fff" stroke-width="1.1"/></svg>www.kestrelhost.com</li>
  </ul>
</section>

<section class="card card--back" aria-label="Business card back">
  <div class="brand"><span class="brand-mark"></span>Kestrel Hosting</div>
</section>

</body>
</html>
```